Vehicle graphics design

An elegant vehicle graphics design for our various vehicles. We are a high end design build renovator/builder.
K240 (white)
Varen Trek (white with black roof)

```html
<!DOCTYPE html>
<html lang="en">
<head>
<meta charset="utf-8">
<title>Halvern Builders – Vehicle Graphics</title>
<link rel="stylesheet" href="https://fonts.googleapis.com/css2?family=Josefin+Sans:wght@600&family=Poppins:wght@500;600&display=swap">
<style>
  :root {
    --navy: #0f2347;
    --copper: #b7712e;
    --white: #ffffff;
    --page: #f3f3f1;
    --panel-edge: #dcdcd8;
  }
  html, body {
    margin: 0;
    width: 1200px;
    height: 1200px;
    overflow: hidden;
    background: var(--page);
  }
  .sheet {
    width: 1200px;
    height: 1200px;
    display: flex;
    flex-direction: column;
    justify-content: center;
    align-items: center;
    gap: 140px;
  }
  .wrap-panel {
    width: 1100px;
    height: 251px;
    display: block;
  }
  .panel-base { fill: var(--white); stroke: var(--panel-edge); stroke-width: 1; }
  .navy { fill: var(--navy); }
  .copper { fill: var(--copper); }
  .brand-name {
    font-family: "Josefin Sans", sans-serif;
    font-weight: 600;
    font-size: 17px;
    letter-spacing: 0.3px;
    fill: var(--navy);
  }
  .web-address {
    font-family: "Poppins", sans-serif;
    font-weight: 500;
    font-size: 9.5px;
    fill: var(--white);
    letter-spacing: 0.3px;
  }
  .phone-number {
    font-family: "Poppins", sans-serif;
    font-weight: 600;
    font-size: 18px;
    letter-spacing: 1.5px;
    fill: var(--white);
  }
</style>
</head>
<body>
<main class="sheet">
  <svg class="wrap-panel" viewBox="230 215 700 160" role="img" aria-label="Halvern Builders side graphics for the K240">
    <rect class="panel-base" x="236" y="220" width="688" height="150" rx="10"/>
    <polygon class="copper" points="452,354 470,354 560,230 542,230"/>
    <polygon class="navy" points="490,354 918,354 918,230 580,230"/>
    <rect class="copper" x="660" y="230" width="258" height="26"/>
    <text class="brand-name" x="250" y="305">HALVERN BUILDERS</text>
    <rect class="copper" x="250" y="329" width="188" height="23"/>
    <text class="web-address" x="258" y="344">www.halvernbuilders.com</text>
    <text class="phone-number" x="676" y="249">403.555.0182</text>
  </svg>

  <svg class="wrap-panel" viewBox="230 215 700 160" role="img" aria-label="Halvern Builders side graphics for the Varen Trek">
    <rect class="panel-base" x="236" y="220" width="688" height="150" rx="10"/>
    <polygon class="copper" points="452,354 470,354 560,230 542,230"/>
    <polygon class="navy" points="490,354 918,354 918,230 580,230"/>
    <rect class="copper" x="660" y="230" width="258" height="26"/>
    <text class="brand-name" x="250" y="305">HALVERN BUILDERS</text>
    <rect class="copper" x="250" y="329" width="188" height="23"/>
    <text class="web-address" x="258" y="344">www.halvernbuilders.com</text>
    <text class="phone-number" x="676" y="249">403.555.0182</text>
  </svg>
</main>
</body>
</html>
```